Thermal Camera flyer

We would like to obtain a sales orientated brochure to promote our two models of thermal imaging cameras as a response to the current Covid 19 health issues. I have provided the text, photos and detailed product specifications , in addition to a sample competitors brochure.
BROCHURE Details : 2 sided - front side to show product, its applications in business, school, hospitals, with text details - Back page to show specifications chart and contact information for Corvel Signal Works. (Melbourne -Sydney-Perth-Brisbane - 1300 647 519
Brochure should be "eye-catching" and reflect the product as a high quality, must-have technology device for todays world.

```html
<!DOCTYPE html>
<html lang="en">
<head>
<meta charset="utf-8">
<title>Technical Specifications – Corvel Signal Works</title>
<link rel="stylesheet" href="https://fonts.googleapis.com/css2?family=Jost:wght@500&family=Arimo:wght@400;700&family=Roboto+Condensed:wght@700&display=swap">
<style>
  :root {
    --paper: #dcdbd0;
    --night: #2b2a36;
    --indigo: #272358;
    --citron: #d8cf3c;
    --ink: #1d1d1f;
    --title: #dedbd2;
    --brand-blue: #2e5aaa;
    --stand-dark: #2a2c38;
    --stand-light: #b9babd;
  }
  * { margin: 0; padding: 0; box-sizing: border-box; }
  html, body { width: 848px; height: 1200px; overflow: hidden; background: var(--paper); }
  .sheet {
    position: relative; width: 848px; height: 1200px; overflow: hidden;
    background: var(--paper); font-family: "Arimo", Arial, sans-serif; color: var(--ink);
  }
  .backdrop { position: absolute; inset: 0; }
  .title {
    position: absolute; top: 96px; left: 0; width: 848px; text-align: center;
    font-family: "Jost", sans-serif; font-weight: 500; font-size: 27px; color: var(--title);
    letter-spacing: 0.2px;
  }
  .product-visual {
    position: absolute; left: 384px; top: 152px; width: 122px; height: 822px;
    border-radius: 8px;
    background: linear-gradient(180deg, var(--stand-dark) 0%, var(--stand-dark) 17%, var(--stand-light) 20%, #d3d4d6 60%, var(--stand-light) 86%, var(--stand-dark) 88%);
  }
  .product-caption {
    position: absolute; top: 978px; left: 0; width: 848px; text-align: center;
    font-size: 11.5px; color: #2a2a2a;
  }
  .spec-col { position: absolute; font-size: 12.6px; line-height: 18.9px; }
  .spec-col.left { right: 489px; text-align: right; }
  .spec-col.right { left: 493px; text-align: left; }
  .spec-block h2 { font-size: 13px; font-weight: 700; line-height: 18.9px; }
  .spec-block p { white-space: nowrap; }
  .camera { top: 319px; }
  .screen { top: 486px; }
  .processor { top: 578px; }
  .interface { top: 652px; }
  .function { top: 319px; }
  .thermal { top: 662px; }
  .brand { position: absolute; left: 497px; top: 1028px; display: flex; align-items: center; gap: 18px; }
  .brand-mark { width: 30px; height: 30px; background: var(--brand-blue); }
  .brand-name { font-size: 20px; font-weight: 400; color: var(--ink); }
  .contact { position: absolute; left: 497px; top: 1075px; font-size: 13px; line-height: 15.8px; }
  .call {
    position: absolute; right: 489px; top: 1094px;
    font-family: "Roboto Condensed", sans-serif; font-weight: 700; font-size: 27px; color: var(--brand-blue);
    white-space: nowrap;
  }
</style>
</head>
<body>
<main class="sheet">
  <svg class="backdrop" width="848" height="1200" viewBox="0 0 848 1200" aria-hidden="true">
    <ellipse cx="330" cy="20" rx="560" ry="276" fill="var(--citron)"/>
    <path d="M380,0 H848 V138 C760,195 620,245 440,252 L380,252 Z" fill="var(--indigo)"/>
    <ellipse cx="390" cy="-30" rx="370" ry="285" fill="var(--night)"/>
    <path d="M0,1044 C180,1010 380,1030 470,1100 C510,1130 540,1165 560,1200 L0,1200 Z" fill="var(--citron)"/>
  </svg>

  <h1 class="title">Technical Specifications</h1>

  <div class="product-visual" role="img" aria-label="Product photo: portable floor standing thermal camera with screen on a tall silver stand and dark base"></div>
  <p class="product-caption">Portable Floor Standing Camera</p>

  <section class="spec-col left spec-block camera">
    <h2>Camera</h2>
    <p>Resolution : 2 million pixels</p>
    <p>Type : Binocular wide dynamic camera</p>
    <p>Aperture : F2.4</p>
    <p>Focusing distance : 50-150cm</p>
    <p>White balance : auto</p>
    <p>Photo flood light :</p>
    <p>LED and IR dual photo flood light</p>
  </section>

  <section class="spec-col left spec-block screen">
    <h2>Screen</h2>
    <p>Size : 8.0 inch IPS LCD screen</p>
    <p>Resolution : 800×1280</p>
    <p>Touch : Not supported</p>
  </section>

  <section class="spec-col left spec-block processor">
    <h2>Processor</h2>
    <p>CPU : QX3288 quad-core</p>
    <p>Storage : EMMC 8G</p>
  </section>

  <section class="spec-col left spec-block interface">
    <h2>Interface</h2>
    <p>Network module :</p>
    <p>Ethernet and wireless (WIFI)</p>
    <p>Audio : 2.5W / 4R speakers</p>
    <p>USB : 1 USB OTG, 1 USB HOST standard A port</p>
    <p>Serial communication : 1 RS232 serial port</p>
    <p>Relay output : 1 door open signal output</p>
    <p>Wiegand One Wiegand :</p>
    <p>26/34 output, one Wiegand 26/34 input</p>
    <p>Upgrade button :</p>
    <p>Support Uboot upgrade button</p>
    <p>Wired network : 1 RJ45 Ethernet socket</p>
  </section>

  <section class="spec-col right spec-block function">
    <h2>Function</h2>
    <p>Face Detection :</p>
    <p>Supports facial detection</p>
    <p>Face library : Up to 30,000</p>
    <p>1: N face recognition : Support</p>
    <p>1: 1 face comparison : Support</p>
    <p>Stranger detection : Support</p>
    <p>Identify distance configuration : Support</p>
    <p>UI interface configuration : Support</p>
    <p>Upgrade remotely: Support</p>
    <p>Interface : I</p>
    <p>nterfaces include device management,</p>
    <p>personnel /photo management,</p>
    <p>record query, etc.</p>
    <p>Deployment method :</p>
    <p>Support public cloud deployment, privatized</p>
    <p>deployment, LAN use, stand-alone use</p>
  </section>

  <section class="spec-col right spec-block thermal">
    <h2>Infrared Imaging Thermal Module</h2>
    <p>Temperature detection : Support</p>
    <p>Temperature detection distance :</p>
    <p>1 meter (optimal distance 0.5 meter)</p>
    <p>Temperature : ≤ ±0.5°C measurement accuracy</p>
    <p>Temperature measurement range : 10°C~42°C</p>
    <p>Pixels : 32 X 32 dots (total 1024 pixels)</p>
    <p>Visitors' temperature is normal and released</p>
    <p>Directly : Support</p>
    <p>Abnormal temperature alarm:</p>
    <p>Support (temperature alarm value can be set)</p>
  </section>

  <div class="brand">
    <span class="brand-mark" aria-hidden="true"></span>
    <span class="brand-name">Corvel Signal Works</span>
  </div>

  <address class="contact" style="font-style: normal;">
    <p>Corvel Signal Works</p>
    <p>Melbourne – Sydney – Perth – Brisbane</p>
    <p>www.corvelsignal.com.au</p>
  </address>

  <p class="call">Call : 1300 647 519</p>
</main>
</body>
</html>
```